Consulting company needs Business Cards - rough concept provided

I'm looking for someone to take our business card idea and make is slick and polished - to communicate our high-end, sophisticated, serious consulting business. We have a rough layout we did in-house. We are open to ideas on repo-ing elements, adjusting sizes, typefaces etc... within the general concept we've already come up with. We want it to be super-clean and sophisticated. We want to keep the white backgrounds, and blue brand colors. Our goal is to print with painted blue edges on thick cardstock. Thank you!!

```html
<!DOCTYPE html>
<html lang="en">
<head>
<meta charset="utf-8">
<title>Northvale Business Cards</title>
<link href="https://fonts.googleapis.com/css2?family=Poppins:wght@400;600;700&display=swap" rel="stylesheet">
<style>
  :root {
    --brand-blue: #0a8fd6;
    --ink: #141414;
    --paper: #ffffff;
    --stage: #8a8a8a;
    --divider: #c9c9c9;
  }
  * { margin: 0; padding: 0; box-sizing: border-box; }
  html, body { width: 1006px; height: 1200px; overflow: hidden; }
  body {
    background: var(--stage);
    font-family: "Poppins", sans-serif;
    color: var(--ink);
    position: relative;
  }
  .card {
    position: absolute;
    left: 64px;
    width: 869px;
    height: 497px;
    background: var(--paper);
    box-shadow: 0 4px 14px rgba(0,0,0,0.35);
  }
  .card--front { top: 40px; }
  .card--back { top: 601px; }

  .frame-line { position: absolute; background: var(--brand-blue); }
  .frame-top { left: 60px; top: 36px; width: 749px; height: 2px; }
  .frame-left { left: 60px; top: 36px; width: 2px; height: 117px; }
  .frame-right { left: 807px; width: 2px; top: 335px; height: 121px; }
  .card--back .frame-right { top: 334px; height: 122px; }
  .frame-bottom { left: 362px; top: 454px; width: 447px; height: 2px; }

  .wordmark {
    position: absolute;
    left: 0; right: 0;
    text-align: center;
    font-weight: 700;
    font-size: 84px;
    line-height: 1;
    letter-spacing: 1px;
    color: var(--brand-blue);
  }
  .card--front .wordmark { top: 70px; }
  .card--back .wordmark { top: 64px; }

  .web-address {
    position: absolute;
    left: 60px;
    top: 442px;
    font-size: 15px;
    letter-spacing: 5.2px;
    color: var(--ink);
  }

  .positioning {
    position: absolute;
    left: 0; right: 0;
    top: 195px;
    text-align: center;
    font-size: 36px;
    line-height: 52px;
    font-weight: 400;
  }
  .positioning strong { color: var(--brand-blue); font-weight: 700; }

  .person { position: absolute; left: 81px; top: 205px; }
  .person-first {
    font-size: 63px; font-weight: 700; line-height: 58px;
    color: var(--brand-blue); letter-spacing: -1px;
  }
  .person-last {
    font-size: 63px; font-weight: 700; line-height: 60px;
    color: var(--ink); letter-spacing: -1px;
  }
  .person-role {
    display: inline-block;
    margin-top: 4px;
    background: var(--brand-blue);
    color: var(--paper);
    font-size: 19px; font-weight: 700;
    line-height: 29px;
    padding: 0 12px;
  }

  .divider {
    position: absolute; left: 455px; top: 218px;
    width: 1px; height: 149px; background: var(--divider);
  }

  .contact { position: absolute; left: 489px; top: 210px; list-style: none; }
  .contact-item {
    position: relative;
    padding-left: 38px;
    font-size: 20px;
    line-height: 24.5px;
    color: var(--ink);
  }
  .contact-item + .contact-item { margin-top: 10px; }
  .contact-icon { position: absolute; left: 0; top: 2px; width: 30px; height: 30px; }
</style>
</head>
<body>

<section class="card card--front">
  <span class="frame-line frame-top"></span>
  <span class="frame-line frame-left"></span>
  <span class="frame-line frame-right"></span>
  <span class="frame-line frame-bottom"></span>
  <div class="wordmark">NORTHVALE</div>
  <p class="positioning">
    <strong>We help</strong> [target demographic] <strong>achieve</strong><br>
    [desired emotional outcome] <strong>by</strong><br>
    [our unique approach] <strong>because</strong><br>
    [our brand beliefs]
  </p>
  <div class="web-address">www.northvale.com</div>
</section>

<section class="card card--back">
  <span class="frame-line frame-top"></span>
  <span class="frame-line frame-left"></span>
  <span class="frame-line frame-right"></span>
  <span class="frame-line frame-bottom"></span>
  <div class="wordmark">NORTHVALE</div>

  <div class="person">
    <div class="person-first">DANA</div>
    <div class="person-last">WHITLOW</div>
    <div class="person-role">BRAND CONSULTANT</div>
  </div>

  <span class="divider"></span>

  <ul class="contact">
    <li class="contact-item">
      <svg class="contact-icon" viewBox="0 0 30 30" aria-hidden="true">
        <circle cx="15" cy="15" r="15" fill="var(--brand-blue)"/>
        <path d="M15 6.5a6 6 0 0 0-6 6c0 4.5 6 11 6 11s6-6.5 6-11a6 6 0 0 0-6-6z" fill="#fff"/>
        <circle cx="15" cy="12.5" r="2.4" fill="var(--brand-blue)"/>
      </svg>
      4820 HARBOR LANE,<br>STE 210 LAKEVIEW,<br>CA 90000
    </li>
    <li class="contact-item">
      <svg class="contact-icon" viewBox="0 0 30 30" aria-hidden="true">
        <circle cx="15" cy="15" r="15" fill="var(--brand-blue)"/>
        <path d="M10 7.5l3 3.2-1.6 2.2c.9 2 2.4 3.5 4.4 4.4l2.2-1.6 3.2 3-1.8 2.6c-5.6-.5-10.6-5.5-11.1-11.1z" fill="#fff"/>
        <path d="M17 8.5a5 5 0 0 1 4.5 4.5M17 5.8a7.6 7.6 0 0 1 7.2 7.2" stroke="#fff" stroke-width="1.4" fill="none" stroke-linecap="round"/>
      </svg>
      (555) 013 4472
    </li>
    <li class="contact-item">
      <svg class="contact-icon" viewBox="0 0 30 30" aria-hidden="true">
        <circle cx="15" cy="15" r="15" fill="var(--brand-blue)"/>
        <rect x="8" y="10" width="14" height="10" fill="#fff"/>
        <path d="M8 10l7 5.5 7-5.5" stroke="var(--brand-blue)" stroke-width="1.3" fill="none"/>
      </svg>
      DANA@NORTHVALE.COM
    </li>
  </ul>

  <div class="web-address">www.northvale.com</div>
</section>

</body>
</html>
```